Software Review & Lead Gen Website Needs a Design

We are starting a software lead generation company in the Appointment Reminder space. Our business model is very similar to toolpicker.net. We get paid when we introduce a qualified buyer to a software vendor by vetting out each buyer with a phone call with one of our experts.

The site needs to entice the buyer to call us or submit a form on our site for a quick interview where we will then narrow down the field of vendors to 3 that best suit their needs. Everything is 100% free for the buyer. We also provide reviews of each software vendor so that they can compare.

The website can currently be found at nudgerated.net (this is a mockup we have just been playing around with - we do not prefer this specific design look, although we do like the font style, icons and color styles)

We're looking for a design of the home page and of the review page (for the reviews, we are going to have a medical reviews page, a dental reviews page, vision reviews page and business reviews page - reminder software will vary depending on the category of the organization) about us, for vendors page, and how it works page.

We've attached some really basic mockups we created of each page in a PDF. Each page is labeled (some have a "2" and that just means as you scroll down) You definitely don't have to copy what we have - we've been told that its too "busy" looking. We feel that a professional web designer could do a much better job of simplifying the UI and creating a better flow as well as just making it more pleasing on the eyes.

For inspiration, see toolpicker.net (they have the exact same business model, but they work in multiple industries whereas we just work with reminder software) and quillhire.net (also a slightly similar model).

Feel free to use the text from our mockups, create your own, or just use latin and we can fill in the rest with what fits best in your design.

We have a logo that we can send you, but no photos, so please use your best judgement and we'll make changes as needed.

Most important to us:

- Strong, simple calls to action - we want the buyers to call us directly, download our buyer's guide (in exchange for their email) or fill out a form for us to call them - when we get them on the phone, we conduct a quick interview to assess their needs and then narrow down the vendors to just 3. The vendors then pay us for the introduction to the buyer.

- Conveys to the visitor how we can help them (narrow down their search, allow them to compare vendors, save time and avoid mistakes)

- Narrow down each visitor by the type of company they are (Medical, Dental, Vision or Business)

We like white space, and simple / modern looks.

Target Market(s)

Doctors offices, office managers and business people

Industry/Entity Type

Software

Font styles to use
Sans Serif

Colors
85abd2
33a6d7
33b7a4
f68d4d
f8ba93
aaaaaa
000000
cfcfcf

Requirements
Must have
• See description above
Nice to have
• We like the font ff-tisa-web-pro and can provide if necessary

```html
<!DOCTYPE html>
<html lang="en">
<head>
<meta charset="utf-8">
<title>Nudge Rated — Appointment Reminder Software Reviews</title>
<link href="https://fonts.googleapis.com/css2?family=Open+Sans:ital,wght@0,300;0,400;0,600;0,700;1,400&display=swap" rel="stylesheet">
<style>
:root{
  --blue:#33a6d7;
  --soft-blue:#85abd2;
  --teal:#33b7a4;
  --orange:#f68d4d;
  --peach:#f8ba93;
  --grey:#aaaaaa;
  --light-grey:#cfcfcf;
  --ink:#000000;
  --text:#555555;
  --dark:#333333;
  --footer:#2b2b2b;
  --band:#efefef;
}
*{box-sizing:border-box;margin:0;padding:0}
html,body{width:1200px;height:2352px;overflow:hidden}
body{font-family:"Open Sans",Arial,sans-serif;color:var(--text);background:#fff;position:relative}
a{text-decoration:none}
.section{position:absolute;left:0;width:1200px}
p{font-size:13px;line-height:21px}

/* header */
.site-header{top:0;height:64px;background:#fff;border-bottom:1px solid #e4e4e4}
.brand{position:absolute;left:60px;top:18px;display:flex;align-items:center;gap:8px;font-size:22px;font-weight:600;color:var(--dark)}
.brand-mark{width:22px;height:22px;background:var(--dark)}
.main-nav{position:absolute;right:60px;top:0;display:flex;height:64px}
.main-nav a{display:block;padding:0 20px;line-height:64px;font-size:12px;font-weight:600;color:var(--dark);letter-spacing:.5px}
.main-nav a.active{background:var(--dark);color:#fff}

/* hero */
.hero{top:64px;height:480px;background:linear-gradient(#f6f6f6,#e9e9e9)}
.hero-title{position:absolute;left:100px;top:66px;width:580px;font-weight:300;font-size:34px;line-height:42px;color:var(--dark);white-space:nowrap}
.hero-title strong{color:var(--blue);font-weight:600}
.hero-text{position:absolute;left:100px;top:164px;width:540px;color:#777}
.hero-screen{position:absolute;left:700px;top:50px;width:400px;height:250px;border-radius:8px;background:linear-gradient(160deg,#d5dde4,#9aa9b5)}
.slide-arrow{position:absolute;top:180px;width:16px;height:30px}
.slide-arrow.prev{left:24px}.slide-arrow.next{right:24px}
.consult{position:absolute;left:300px;top:330px;width:600px;height:92px;background:#fff;border:1px solid var(--light-grey);display:flex;align-items:center;justify-content:space-between;padding:0 28px}
.consult p{font-size:15px;line-height:22px;color:var(--dark)}
.consult .phone{color:var(--orange);font-weight:700;font-size:19px}
.btn{display:inline-block;color:#fff;font-weight:600;font-size:13px;letter-spacing:.5px;text-align:center;border-radius:3px}
.btn-teal{background:var(--teal)}
.btn-blue{background:var(--blue)}
.btn-dark{background:#4a4a4a;font-size:10px;padding:7px 10px;border-radius:2px}
.consult .btn{padding:14px 26px}

/* categories */
.categories{top:544px;height:344px;text-align:center}
.section-title{font-size:30px;font-weight:300;color:var(--blue);position:absolute;left:0;width:1200px;text-align:center}
.categories .section-title{top:50px}
.category{position:absolute;top:120px;width:160px;text-align:center}
.category svg{width:120px;height:120px}
.category span{display:block;margin-top:14px;font-size:20px;font-weight:300;color:var(--dark)}

/* testimonials */
.testimonials{top:888px;height:332px;background:var(--band);border-top:1px solid #e0e0e0;border-bottom:1px solid #e0e0e0}
.testimonials .section-title{top:44px;color:#777}
.testimonials .section-title em{font-style:normal;color:var(--teal)}
.avatar{position:absolute;left:130px;top:130px;width:96px;height:96px;border-radius:50%;background:linear-gradient(135deg,#c79a7c,#6a4b3b)}
.quote{position:absolute;left:250px;top:130px;width:820px;font-style:italic;color:#777}
.quote cite{display:block;margin-top:8px;font-style:normal;font-weight:600;color:var(--orange)}
.testimonials .slide-arrow{top:160px}

/* review cards */
.review-row{top:1220px;height:160px;display:flex;gap:20px;padding:24px 100px 0}
.review-card{flex:1}
.review-card p{font-size:11px;line-height:17px;font-style:italic;color:#888;text-align:center;height:48px}
.review-card .actions{display:flex;gap:6px;justify-content:center;margin-top:10px}

/* content */
.content{top:1380px;height:812px}
.intro{position:absolute;left:100px;top:20px;width:680px}
.intro p{margin-bottom:12px;font-size:12px;line-height:19px}
.intro a{color:var(--orange)}
.lead-form{position:absolute;left:100px;top:210px;width:680px;height:560px;background:#fdf3ec;border:1px solid var(--peach);padding:28px}
.lead-form h2{font-size:24px;font-weight:400;color:var(--orange);line-height:32px;width:560px}
.lead-form .copy{position:absolute;left:28px;top:120px;width:310px}
.lead-form .copy p{font-size:12px;line-height:19px;margin-bottom:12px}
.fields{position:absolute;left:370px;top:118px;width:280px}
.field{height:34px;margin-bottom:10px;background:#fff;border:1px solid var(--light-grey);font-size:11px;color:var(--grey);line-height:32px;padding:0 10px;position:relative}
.field.select::after{content:"";position:absolute;right:10px;top:14px;border:5px solid transparent;border-top-color:var(--grey)}
.lead-form .btn{position:absolute;left:28px;top:470px;padding:14px 34px;font-size:15px}

.sidebar{position:absolute;left:820px;top:20px;width:280px}
.guide{border:1px solid var(--peach);padding:18px;height:320px;position:relative}
.guide h3{font-size:22px;font-weight:400;color:var(--orange)}
.guide .sub{font-size:11px;font-weight:600;color:var(--dark);margin-top:4px}
.guide-art{margin:14px auto 0;width:200px;height:150px;background:linear-gradient(135deg,#bfe6dc,#6fc3b2)}
.guide .btn{display:block;margin-top:16px;padding:12px 0}
.report{margin-top:26px}
.report h3{font-size:22px;font-weight:400;color:var(--orange);margin-bottom:14px}
.report article{margin-bottom:20px}
.report h4{font-size:13px;font-weight:600;color:var(--blue);line-height:18px}
.report p{font-size:11px;line-height:17px;margin-top:6px}

/* footer */
.site-footer{top:2192px;height:160px;background:var(--footer);color:#aaa;font-size:11px}
.footer-brand{position:absolute;left:100px;top:26px;line-height:18px}
.social{position:absolute;left:100px;top:74px;display:flex;gap:8px;align-items:center}
.social i{display:block;width:26px;height:26px;border-radius:50%;background:#555}
.social span{margin-left:8px}
.footer-cols{position:absolute;left:420px;top:26px;display:flex;gap:50px}
.footer-cols h5{font-size:12px;font-weight:600;color:#fff;margin-bottom:6px}
.footer-cols ul{list-style:none}
.footer-cols li{line-height:17px}
.footer-cols .hot{color:var(--orange);font-weight:700}
.footer-bar{position:absolute;left:0;bottom:0;width:1200px;height:20px;background:#1f1f1f}
</style>
</head>
<body>

<header class="section site-header">
  <div class="brand"><span class="brand-mark"></span>nudge rated</div>
  <nav class="main-nav">
    <a class="active" href="#">REVIEWS</a><a href="#">ABOUT US</a><a href="#">BLOG</a><a href="#">CONTACT</a>
  </nav>
</header>

<section class="section hero">
  <h1 class="hero-title"><strong>The Authority</strong> on<br>Appointment Reminder Software</h1>
  <p class="hero-text">Compare in-depth reviews, see pricing and demos, and get expert advice on reminder software. Narrow your shortlist down to the three vendors that fit your office best, and save hours of research time with a quick, free call.</p>
  <div class="hero-screen" role="img" aria-label="Laptop showing the review site home page"></div>
  <svg class="slide-arrow prev" viewBox="0 0 16 30"><path d="M14 2 2 15l12 13" fill="none" stroke="#999" stroke-width="3"/></svg>
  <svg class="slide-arrow next" viewBox="0 0 16 30"><path d="M2 2l12 13L2 28" fill="none" stroke="#999" stroke-width="3"/></svg>
  <div class="consult">
    <p>We'll help determine which<br>patient reminder service is best for you<br><span class="phone">Call us at 555-555-5555</span></p>
    <a class="btn btn-teal" href="#">FREE CONSULTATION</a>
  </div>
</section>

<section class="section categories">
  <h2 class="section-title">Compare Reviews by Category</h2>
  <div class="category" style="left:185px">
    <svg viewBox="0 0 120 120"><circle cx="60" cy="60" r="58" fill="var(--blue)"/><path d="M42 36c8-4 12 2 18 2s10-6 18-2c10 6 6 22 2 30-3 8-3 22-8 22-6 0-5-18-12-18s-6 18-12 18c-5 0-5-14-8-22-4-8-8-24 2-30z" fill="#fff"/></svg>
    <span>Dental</span>
  </div>
  <div class="category" style="left:435px">
    <svg viewBox="0 0 120 120"><circle cx="60" cy="60" r="58" fill="#e25050"/><path d="M50 30h20v20h20v20H70v20H50V70H30V50h20z" fill="#fff"/></svg>
    <span>Medical</span>
  </div>
  <div class="category" style="left:685px">
    <svg viewBox="0 0 120 120"><circle cx="60" cy="60" r="58" fill="var(--teal)"/><path d="M24 60c10-16 22-24 36-24s26 8 36 24c-10 16-22 24-36 24S34 76 24 60z" fill="#fff"/><circle cx="60" cy="60" r="13" fill="var(--dark)"/></svg>
    <span>Vision</span>
  </div>
  <div class="category" style="left:935px">
    <svg viewBox="0 0 120 120"><circle cx="60" cy="60" r="58" fill="#4a4a4a"/><rect x="42" y="28" width="36" height="64" fill="#fff"/><g fill="#4a4a4a"><rect x="48" y="36" width="8" height="8"/><rect x="64" y="36" width="8" height="8"/><rect x="48" y="52" width="8" height="8"/><rect x="64" y="52" width="8" height="8"/><rect x="48" y="68" width="8" height="8"/><rect x="64" y="68" width="8" height="8"/><rect x="55" y="80" width="10" height="12"/></g></svg>
    <span>Business</span>
  </div>
</section>

<section class="section testimonials">
  <h2 class="section-title">Clients <em>Testimonials</em></h2>
  <svg class="slide-arrow prev" viewBox="0 0 16 30"><path d="M14 2 2 15l12 13" fill="none" stroke="#999" stroke-width="3"/></svg>
  <svg class="slide-arrow next" viewBox="0 0 16 30"><path d="M2 2l12 13L2 28" fill="none" stroke="#999" stroke-width="3"/></svg>
  <div class="avatar" role="img" aria-label="Portrait photo of the client"></div>
  <blockquote class="quote">
    <p>“ Within one short call the team understood how our practice books patients, and they sent us three vendors that truly fit. We compared reviews side by side, sat through two demos, and had a new reminder system live in under a month. No-shows dropped noticeably within weeks, and the whole process cost us nothing at all. ”</p>
    <cite>John Doe</cite>
  </blockquote>
</section>

<section class="section review-row">
  <div class="review-card"><p>“ Simple setup, clean text reminders and a friendly support team that answers fast. ”</p><div class="actions"><a class="btn btn-dark" href="#">IN DEPTH ANALYSIS</a><a class="btn btn-dark" href="#">USER REVIEWS</a></div></div>
  <div class="review-card"><p>“ Strong scheduling sync and flexible voice calls, though pricing is a bit higher. ”</p><div class="actions"><a class="btn btn-dark" href="#">IN DEPTH ANALYSIS</a><a class="btn btn-dark" href="#">USER REVIEWS</a></div></div>
  <div class="review-card"><p>“ Great for busy clinics that need email, text and voice in one dashboard. ”</p><div class="actions"><a class="btn btn-dark" href="#">IN DEPTH ANALYSIS</a><a class="btn btn-dark" href="#">USER REVIEWS</a></div></div>
  <div class="review-card"><p>“ Affordable plans for small offices with reliable delivery and clear reports. ”</p><div class="actions"><a class="btn btn-dark" href="#">IN DEPTH ANALYSIS</a><a class="btn btn-dark" href="#">USER REVIEWS</a></div></div>
</section>

<section class="section content">
  <div class="intro">
    <p>Choosing reminder software should not take weeks. Our experts follow every major vendor, test new features, and talk with offices like yours every day. We know which tools work for a small dental office and which suit a large multi-site medical group.</p>
    <p>Tell us how you schedule, how many patients you see and which systems you already use. We listen, ask a few short questions, and match you with the three vendors most likely to fit your budget and workflow.</p>
    <p>Everything we do is free for buyers. <a href="#">Vendors pay us for introductions, so you always get honest advice at no cost.</a></p>
  </div>

  <div class="lead-form">
    <h2>Get Introduced to the Top-Rated Reminder Services In Seconds</h2>
    <div class="copy">
      <p>Share a few details about your office and one of our experts will call you for a quick, friendly interview about your needs.</p>
      <p>We narrow the field to three vendors, set up the demos you want and send you pricing so you can compare side by side.</p>
      <p>No pressure and no cost. Most calls take less than ten minutes.</p>
    </div>
    <div class="fields">
      <div class="field">Your Company Name</div>
      <div class="field">First Name</div>
      <div class="field">Last Name</div>
      <div class="field">E-mail</div>
      <div class="field">Phone</div>
      <div class="field select">Organization Type</div>
      <div class="field">Note</div>
    </div>
    <a class="btn btn-blue" href="#">SHOW ME THE MONEY!</a>
  </div>

  <aside class="sidebar">
    <div class="guide">
      <h3>Free PDF Guide :</h3>
      <p class="sub">Ultimate Reminder Service Buyer's Guide</p>
      <div class="guide-art" role="img" aria-label="Illustration of the buyer's guide booklet"></div>
      <a class="btn btn-teal" href="#">GET BUYER'S GUIDE</a>
    </div>
    <div class="report">
      <h3>Reminder Report</h3>
      <article>
        <h4>Top 5 HIPAA Questions - Answered</h4>
        <p>What every office should ask before sending patient reminders by text, email or voice.</p>
      </article>
      <article>
        <h4>The Future of Patient Engagement Requires A Look Into The Past</h4>
        <p>Why the simple phone call still matters in a world of apps and automated messages.</p>
      </article>
    </div>
  </aside>
</section>

<footer class="section site-footer">
  <div class="footer-brand">Copyright © 2014 Nudge Rated.<br>All rights reserved.</div>
  <div class="social"><i></i><i></i><i></i><span>Privacy &nbsp;|&nbsp; Terms of Use</span></div>
  <div class="footer-cols">
    <div><h5>Who we are</h5><ul><li>About Us</li><li>How it Works</li><li>Blog</li></ul></div>
    <div><h5>For Vendors</h5><ul><li>Vendor Tool</li><li>Let's Connect</li></ul></div>
    <div><h5>For Buyers</h5><ul><li>Medical</li><li>Dental</li><li>Vision</li><li>Business</li><li class="hot">FREE ADVICE</li></ul></div>
    <div><h5>Resources</h5><ul><li>Buyer's Guide</li><li>How we Grade</li><li>Contact Us</li><li>555-555-5555</li></ul></div>
  </div>
  <div class="footer-bar"></div>
</footer>

</body>
</html>
```